Podcast Graphics For Internet Business Building Podcast

We need new podcast graphics.
1400x1400
300dpi

Needs to include text "Quiet Harbor Ledger Hour" as the podcast title and "Creative Internet Income Strategies" as a subtitle.

We like blue and grey as our main colors, but are open to other schemes.

Please see attached image for an example of podcast graphics we like. While we prefer a more plain look, it would be nice to have a subtle hint related to a "machine" in the background. Something like a pencil sketch of cogs like on the Quiet Harbor Ledger 10 book cover (attached image).

Target Market(s)

online entrepreneurs or those who want to start an online business

Font styles to use
Sans Serif

Colors
0455a3
3277b5

Requirements
Must have
• Text noted in project description
Should not have
• No money symbols or flashy "make money" type things.

```html
<!DOCTYPE html>
<html lang="en">
<head>
<meta charset="utf-8">
<title>Quiet Harbor Ledger Hour — Podcast Cover</title>
<link href="https://fonts.googleapis.com/css2?family=Bebas+Neue&display=swap" rel="stylesheet">
<style>
  :root {
    --page: #ffffff;
    --navy-deep: #111a3a;
    --navy: #0b3a6e;
    --brand-blue: #0455a3;
    --brand-blue-bright: #0566ae;
    --teal-field: #0487b1;
    --stripe-light: #b3b4b6;
    --stripe-dark: #808184;
    --figure-light: #9aa3ad;
    --figure-dark: #4a4f57;
    --type: #ffffff;
  }
  html, body {
    margin: 0;
    padding: 0;
    width: 1177px;
    height: 1200px;
    overflow: hidden;
    background: var(--page);
  }
  .cover {
    position: absolute;
    left: 153px;
    top: 138px;
    width: 896px;
    height: 896px;
    display: block;
  }
  .cover-title {
    font-family: "Bebas Neue", "Oswald", sans-serif;
    font-size: 138px;
    fill: var(--type);
  }
  .cover-subtitle {
    font-family: "Bebas Neue", "Oswald", sans-serif;
    font-size: 53px;
    fill: var(--type);
  }
</style>
</head>
<body>
  <svg class="cover" viewBox="0 0 896 896" xmlns="http://www.w3.org/2000/svg">
    <defs>
      <linearGradient id="band-top" x1="0" y1="0" x2="1" y2="0">
        <stop offset="0" stop-color="var(--navy-deep)"/>
        <stop offset="1" stop-color="var(--brand-blue-bright)"/>
      </linearGradient>
      <linearGradient id="band-top-lip" x1="0" y1="0" x2="1" y2="0">
        <stop offset="0" stop-color="var(--brand-blue-bright)"/>
        <stop offset="1" stop-color="var(--navy-deep)"/>
      </linearGradient>
      <linearGradient id="band-bottom" x1="0" y1="0" x2="1" y2="0">
        <stop offset="0" stop-color="var(--brand-blue-bright)"/>
        <stop offset="0.55" stop-color="var(--navy)"/>
        <stop offset="1" stop-color="var(--navy-deep)"/>
      </linearGradient>
      <linearGradient id="stripe" x1="0" y1="1" x2="1" y2="0">
        <stop offset="0" stop-color="var(--stripe-light)"/>
        <stop offset="1" stop-color="var(--stripe-dark)"/>
      </linearGradient>
      <linearGradient id="figure-tone" x1="0" y1="0" x2="0" y2="1">
        <stop offset="0" stop-color="var(--figure-dark)"/>
        <stop offset="0.5" stop-color="var(--figure-light)"/>
        <stop offset="1" stop-color="var(--figure-dark)"/>
      </linearGradient>
    </defs>

    <!-- background field -->
    <rect class="field" x="0" y="0" width="896" height="896" fill="var(--teal-field)"/>

    <!-- top band -->
    <rect class="band-top-lip" x="0" y="0" width="896" height="166" fill="url(#band-top-lip)"/>
    <polygon class="band-top" points="0,0 896,0 896,50 843,126 0,126" fill="url(#band-top)"/>

    <!-- bottom band -->
    <rect class="band-bottom" x="0" y="721" width="896" height="175" fill="url(#band-bottom)"/>

    <!-- grey diagonal stripes -->
    <polygon class="stripe" points="119,0 257,0 0,266 0,126" fill="url(#stripe)"/>
    <polygon class="stripe" points="227,702 367,702 384,721 175,896 35,896" fill="url(#stripe)"/>

    <!-- illustration area -->
    <rect class="illustration" x="567" y="126" width="196" height="664" rx="6"
          fill="url(#figure-tone)" opacity="0.55"
          role="img" aria-label="Illustration: a team of businessmen lifting one another to screw in a glowing light bulb hanging from a lamp fixture"/>

    <!-- title -->
    <text class="cover-title" x="134" y="305">QUIET</text>
    <text class="cover-title" x="134" y="426">HARBOR</text>
    <text class="cover-title" x="134" y="548">LEDGER</text>
    <text class="cover-title" x="134" y="669">HOUR</text>

    <!-- subtitle -->
    <text class="cover-subtitle" x="250" y="788">CREATIVE INTERNET</text>
    <text class="cover-subtitle" x="485" y="840">INCOME STRATEGIES</text>
  </svg>
</body>
</html>
```